Product sheet for medical device dedicated to clinicians and researchers

We need a product sheet based in 1-pager format (1 page recto only or 1 page recto verso). The elements expected in the product sheet are in the DOCX file enclosed. We also enclosed some assets that could be useful.
Requirements:
- This is a technical document, not a commercial/shiny document. Pictures from the photoshoot can be used but it is not the main information.
- The focus is on the clarity and the readability of the information.
- The text must be searchable.
- The design must follow the brand book enclosed.
- We need a PDF document AND the source file (Adobe InDesign ideally) for further modifications.
We are able to provide additional information & potential assets if required.
Target Market(s)
Clinicians and researchers in healthcare
Industry/Entity Type
Healthcare
Font styles to use
Other font styles liked:
- See brandbook
Colors
Designer to choose colors to be used in the design.
Look and feel

```html
<!DOCTYPE html>
<html lang="en">
<head>
<meta charset="utf-8">
<title>Nuvi Childwave for Research – Product Sheet</title>
<link rel="stylesheet" href="https://fonts.googleapis.com/css2?family=Poppins:wght@400;500;600;700;800&display=swap">
<style>
  :root {
    --canvas: #e2e5e6;
    --paper: #ffffff;
    --ink: #111a22;
    --navy: #062a40;
    --brand-blue: #0e5a83;
    --header-top: #0d5b82;
    --header-bottom: #083a5a;
    --table-head: #cdebee;
    --row-alt: #e4e6e8;
    --rule: #2b3d4a;
  }
  * { box-sizing: border-box; margin: 0; padding: 0; }
  html, body { width: 1028px; height: 1200px; overflow: hidden; }
  body {
    background: var(--canvas);
    font-family: "Poppins", sans-serif;
    color: var(--ink);
  }
  .sheet {
    position: absolute; left: 50px; top: 0;
    width: 927px; height: 1200px;
    background: var(--paper);
    overflow: hidden;
  }
  .hero {
    position: absolute; left: 0; top: 0; width: 927px; height: 291px;
    background: linear-gradient(160deg, var(--header-top) 0%, var(--header-bottom) 70%, #0a4468 100%);
  }
  .hero-title {
    position: absolute; left: 36px; top: 44px;
    color: #fff; font-weight: 800; font-size: 66px; line-height: 76px; letter-spacing: -1.3px;
  }
  .hero-pill {
    position: absolute; left: 0; top: 212px; width: 434px; height: 60px;
    background: #fff; border-radius: 0 30px 30px 0;
  }
  .hero-pill span {
    position: absolute; left: 36px; top: 3px;
    color: var(--brand-blue); font-weight: 700; font-size: 49px; line-height: 56px; letter-spacing: -0.5px;
  }
  .hero-photo {
    position: absolute; left: 475px; top: 56px; width: 354px; height: 240px;
    border: 6px solid #1c1d20; border-bottom-width: 10px; border-radius: 10px 10px 0 0;
    background: linear-gradient(135deg, #e9e4dc 0%, #cfc8bd 50%, #a9b4bd 100%);
  }
  .hero-base {
    position: absolute; left: 437px; top: 296px; width: 430px; height: 11px;
    background: linear-gradient(#8a8d91, #4a4d52); border-radius: 0 0 8px 8px;
  }
  .intro { position: absolute; left: 38px; top: 300px; width: 830px; }
  .section-title { font-weight: 800; font-size: 21px; line-height: 26px; letter-spacing: -0.3px; }
  .intro p { font-size: 15px; line-height: 18.5px; margin-top: 7px; }
  .intro .label { font-weight: 700; font-size: 13px; margin-top: 12px; }
  .component { position: absolute; left: 38px; width: 840px; }
  .component svg { position: absolute; left: 0; top: 1px; width: 34px; height: 34px; }
  .component p { margin-left: 46px; font-size: 15px; line-height: 18.5px; }
  .component b { font-weight: 700; }
  .box-band {
    position: absolute; left: 0; top: 614px; width: 310px; height: 46px;
    background: var(--navy); border-radius: 0 23px 23px 0;
    color: #fff; font-weight: 800; font-size: 21px; line-height: 46px; padding-left: 37px;
  }
  .box-lead {
    position: absolute; left: 321px; top: 628px; font-weight: 700; font-size: 15px; line-height: 20px;
  }
  .box-rule { position: absolute; left: 551px; top: 640px; width: 376px; height: 1px; background: var(--rule); }
  .kit { position: absolute; top: 700px; text-align: center; font-size: 15px; line-height: 18.5px; }
  .kit svg { display: block; margin: 0 auto 18px; width: 60px; height: 52px; }
  .kit-divider { position: absolute; top: 749px; width: 2px; height: 58px; background: var(--ink); }
  .data-rule { position: absolute; left: 13px; top: 869px; width: 565px; height: 1px; background: var(--rule); }
  .data-band {
    position: absolute; left: 575px; top: 844px; width: 352px; height: 46px;
    background: var(--navy); border-radius: 23px 0 0 23px;
    color: #fff; font-weight: 800; font-size: 21px; line-height: 46px; padding-left: 27px;
  }
  .vitals {
    position: absolute; left: 38px; top: 912px; width: 851px;
    border-collapse: collapse; font-size: 15px;
  }
  .vitals th, .vitals td { border: 1px solid #3b4b57; text-align: left; padding: 0 0 0 17px; }
  .vitals th { background: var(--table-head); font-weight: 700; height: 35px; font-size: 14.5px; }
  .vitals td { height: 36.5px; }
  .vitals tr:nth-child(even) td { background: var(--row-alt); }
  .footer {
    position: absolute; left: 0; top: 1154px; width: 927px; height: 46px;
    background: var(--navy); color: #fff; text-align: center;
    font-weight: 600; font-size: 15px; line-height: 46px;
  }
</style>
</head>
<body>
<main class="sheet">
  <header class="hero">
    <h1 class="hero-title">NUVI<br>CHILDWAVE</h1>
    <div class="hero-pill"><span>FOR RESEARCH</span></div>
    <div class="hero-photo" role="img" aria-label="Laptop screen showing a parent holding a baby while a doctor reviews a chart in a clinic"></div>
    <div class="hero-base"></div>
  </header>

  <section class="intro">
    <h2 class="section-title">WHAT IS NUVI CHILDWAVE?</h2>
    <p>Nuvi Childwave is a comprehensive solution to record and collect health data from the pediatric population from 0-12 years old. While initially designed for pediatrics, the solution works on older children and on adults.</p>
    <p class="label">NUVI CHILDWAVE IS COMPOSED BY:</p>
  </section>

  <div class="component" style="top:418px">
    <svg viewBox="0 0 34 34" fill="#0e3550"><circle cx="13" cy="9" r="6"/><path d="M2 31c0-8 5-13 11-13s11 5 11 13z"/><path d="M22 5l6 6-3 7 5 4-4 8" fill="none" stroke="#0e3550" stroke-width="1.6" stroke-dasharray="2 2"/></svg>
    <p><b>The Nuvi Band:</b> A sensor to collect and interpret biometric signals and send over Bluetooth Low Energy to Nuvi Monitor. The Nuvi Band is fitted on the upper-arm of the participant.</p>
  </div>
  <div class="component" style="top:470px">
    <svg viewBox="0 0 34 34" fill="none" stroke="#0e3550" stroke-width="2.4"><rect x="2" y="5" width="30" height="20" rx="2"/><circle cx="11" cy="14" r="4"/><path d="M14 17l4 4M21 19v-5M25 19v-8M29 19v-3M13 30h9M17 25v5"/></svg>
    <p><b>The Nuvi Monitor:</b> A dedicated tablet with the Nuvi Monitor App to collect the data from the Nuvi Band and send it over WiFi on the Nuvi Cloud.</p>
  </div>
  <div class="component" style="top:522px">
    <svg viewBox="0 0 34 34"><path d="M8 24a7 7 0 0 1 1-14 9 9 0 0 1 17 2 6 6 0 0 1 0 12z" fill="#0e3550"/><path d="M17 16l7 3v5c0 4-3 7-7 8-4-1-7-4-7-8v-5z" fill="#fff" stroke="#0e3550" stroke-width="2"/><path d="M14 24l2 2 4-4" fill="none" stroke="#0e3550" stroke-width="2"/></svg>
    <p><b>The Nuvi Cloud:</b> A secured cloud environment to store and consolidate the collected data.</p>
  </div>
  <div class="component" style="top:570px">
    <svg viewBox="0 0 34 34"><rect x="8" y="2" width="20" height="18" fill="none" stroke="#0e3550" stroke-width="2"/><path d="M12 7h12M12 11h12M12 15h8" stroke="#0e3550" stroke-width="2"/><rect x="6" y="18" width="22" height="15" fill="#0e3550"/><rect x="9" y="27" width="6" height="2" fill="#fff"/></svg>
    <p><b>The Nuvi Analytics:</b> A web portal to visualize the collected data and the trends..</p>
  </div>

  <div class="box-band">WHAT’S IN THE BOX?</div>
  <div class="box-lead">The Nuvi kit is composed by:</div>
  <div class="box-rule"></div>

  <div class="kit" style="left:42px;width:130px">
    <svg viewBox="0 0 60 52" fill="none" stroke="#0e3550" stroke-width="4" stroke-linecap="round"><circle cx="30" cy="26" r="7" fill="#0e3550"/><path d="M19 15a15 15 0 0 0 0 22M41 15a15 15 0 0 1 0 22M11 7a26 26 0 0 0 0 38M49 7a26 26 0 0 1 0 38"/></svg>
    The Nuvi Band<br>(the sensor<br>unit).
  </div>
  <div class="kit-divider" style="left:186px"></div>
  <div class="kit" style="left:196px;width:200px">
    <svg viewBox="0 0 60 52" fill="none" stroke="#0e3550" stroke-width="3"><ellipse cx="30" cy="20" rx="15" ry="15"/><circle cx="30" cy="20" r="6" fill="#0e3550"/><path d="M30 35v15M8 40h12M40 40h12M10 45h8M42 45h8"/></svg>
    4 textile bracelets (S, M, L<br>and XL) to adapt to the<br>different morphology.
  </div>
  <div class="kit-divider" style="left:403px"></div>
  <div class="kit" style="left:410px;width:190px">
    <svg viewBox="0 0 60 52" fill="none" stroke="#0e3550" stroke-width="3"><rect x="4" y="3" width="44" height="32" rx="2"/><path d="M10 10h18M10 15h18M10 20h14M20 42h14M27 35v7"/><rect x="34" y="14" width="20" height="30" rx="3" fill="#fff"/><path d="M39 29l3 3 6-6"/></svg>
    The Nuvi Monitor tablet<br>with the Nuvi Monitor<br>App pre-installed.
  </div>
  <div class="kit-divider" style="left:612px"></div>
  <div class="kit" style="left:625px;width:140px">
    <svg viewBox="0 0 60 52" fill="none" stroke="#0e3550" stroke-width="4" stroke-linecap="round"><path d="M16 22v18a7 7 0 0 0 14 0V12a7 7 0 0 1 14 0v18"/><rect x="12" y="8" width="8" height="14" rx="1" fill="#0e3550"/><rect x="40" y="30" width="8" height="12" rx="1" fill="#0e3550"/></svg>
    2x USB cables<br>(for the band<br>and the tablet).
  </div>
  <div class="kit-divider" style="left:768px"></div>
  <div class="kit" style="left:776px;width:114px">
    <svg viewBox="0 0 60 52" fill="#0e3550"><rect x="10" y="26" width="10" height="24"/><rect x="25" y="26" width="10" height="24"/><rect x="40" y="26" width="10" height="24"/><rect x="44" y="4" width="3" height="18"/><rect x="26" y="6" width="8" height="16"/><path d="M10 4l5 10 5-10" fill="none" stroke="#0e3550" stroke-width="3"/></svg>
    2x USB<br>charger for<br>power outlet.
  </div>

  <div class="data-rule"></div>
  <div class="data-band">HEALTH DATA COLLECTED</div>

  <table class="vitals">
    <colgroup><col style="width:174px"><col style="width:185px"><col style="width:186px"><col style="width:306px"></colgroup>
    <thead><tr><th>VITAL SIGNS</th><th>RANGE</th><th>ACCURACY</th><th>FREQUENCY</th></tr></thead>
    <tbody>
      <tr><td>Pulse rate</td><td>25 to 250 bpm</td><td>±3 bpm RMSE (*)</td><td>1 data point per sec</td></tr>
      <tr><td>SpO2</td><td>50 to 100%</td><td>±3.5% RMSE (*)</td><td>1 data point per sec</td></tr>
      <tr><td>Respiratory rate</td><td>3 to 70 BrPM</td><td>± 3 BrPM RMSE</td><td>1 data point per sec</td></tr>
      <tr><td>Skin temperature</td><td>0 to 50°C</td><td>± 0.01°C</td><td>1 data point per 5 sec</td></tr>
      <tr><td>Actigraphy</td><td>0 to 2G</td><td>±0.001G</td><td>3 data points (X, Y, Z) per 100</td></tr>
    </tbody>
  </table>

  <footer class="footer">(*) FDA cleared signal processing algorithm</footer>
</main>
</body>
</html>
```